Stand up pouch design for dog treats seafood & pasture themed (logo supplied)

We require a universal packaging design (front and back only) that can be used for multiple products across our range of dog treats.
Our company specialises in making air-dried, natural treats for dogs. Our product range includes seafood (sardines, whitebait, mussels) and meat products (liver, heart, kidney).
The packaging is to be used on stand up pouches such as these:
https://pouchworkshop.example.com.au/product/upright-bags-70g/
I currently do not have a template, however, you can assume the size will be similar to the one mentioned above (height 170, width 110). I will ask the printers to modify the design to fit into their templates when we are ready to print.
The design will need to be scalable to 150g and 250g bags, however, I don't think that will be a major issue as that is kept in mind as everything can just be enlarged.
The design will need to have a clear window at the front, similar to the koru picture here:
https://www.hounddepot.example.com.au/hounddepot-assets/images/products/p/koru-ridge-dry-dog-food-lamb.png
The clear window shouldn't be too large similar to how the koru one is quite small, as we need the bag to be opaque to protect the protein inside.
Our photoshop files for the logo are attached for reference in terms of style and colours.
The packaging should allow changing of the picture in the background on the front of the packaging to correspond with the type of protein that is being sold.
For example, the koru one has lamb in the back for lamb products, we would like to do the same.
We will require 4 background images that can be changed depending on the protein - sardines, NZ green lip mussels, whitebait, pasture with cows (this is for organ meats)
The back of the packaging should have a number of panels for us to place text, the design on the back can be static (no changing of the picture to correspond with protein type).
The placeholder text for the front and back of the package can be found here for each type (can just use 1 as placeholder example for design of the back):
https://barneysnacko.example.com.au/shop/premium-australian-caught-whitebait-dog-treats/
https://barneysnacko.example.com.au/shop/premium-australian-grass-fed-beef-heart-dog-treats/
https://barneysnacko.example.com.au/shop/premium-australian-caught-sardine-dog-treats/
https://barneysnacko.example.com.au/shop/premium-new-zealand-green-lip-mussel-dog-treats/
https://barneysnacko.example.com.au/shop/premium-australian-grass-fed-beef-kidney-dog-treats/
https://barneysnacko.example.com.au/shop/premium-australian-grass-fed-beef-liver-dog-treats/
For each product, we also have some icons and text (air-dried, single ingredient, etc) that we would like to have on the back of the bag. The icons and text can be found on the placeholder text mentioned above (example screenshot is attached).
Please also include weight in grams on the front.
The feel of the packaging should be clean, healthy and natural using the tones that are similar to our logo.
I've attached the packaging example that we like from koru, please do not copy the exact feel of the design in terms of colour or shape as we do not want too look too similar to that brand.
What we require:
1. Front design
2. Back design
3. 6 rendered images (of each product, with different backgrounds) of the front design on pouches that we can use on the website as product images.
Target Market(s)
Dog owners/lovers who want to purchase premium treats for their dogs
Industry/Entity Type
Dog treats

```html
<!DOCTYPE html>
<html lang="en">
<head>
<meta charset="utf-8">
<title>Barney's Dog Treats – Pouch Designs</title>
<link rel="stylesheet" href="https://fonts.googleapis.com/css2?family=Josefin+Sans:wght@400;600;700&family=Playfair+Display:ital,wght@1,700&family=Quicksand:wght@400;500;600&display=swap">
<style>
:root{
  --canvas:#ffffff;
  --beef-red:#8e1c1a;
  --beef-strip:#6a1513;
  --sea-blue:#0f3d5c;
  --sea-strip:#8fb9a2;
  --amber:#c6853c;
  --amber-dark:#a96a28;
  --cream:#f4ead8;
  --brown:#6b3a1f;
  --white:#ffffff;
  --ink-soft:rgba(255,255,255,.85);
}
*{box-sizing:border-box;margin:0;padding:0}
html,body{width:1200px;height:651px;overflow:hidden;background:var(--canvas)}
.canvas{position:relative;width:1200px;height:651px}
.pouch{position:absolute;top:99px;width:284px;height:430px;border-radius:3px 3px 12px 12px;overflow:hidden;color:var(--white);font-family:"Quicksand",sans-serif}
.pouch--beef{left:87px;background:var(--beef-red)}
.pouch--back{left:445px;background:var(--sea-blue)}
.pouch--mussels{left:800px;background:var(--sea-blue)}
.zip-line{position:absolute;left:12px;right:12px;top:50px;height:2px;background:rgba(0,0,0,.18)}
.brand-tab{position:absolute;left:93px;width:106px;top:0;height:48px;background:var(--amber);border-radius:0 0 10px 10px;border:1.5px solid var(--cream);border-top:none}
.brand-seal{position:absolute;left:106px;top:18px;width:80px;height:80px;border-radius:50%;background:var(--cream);border:3px solid var(--white);display:flex;align-items:center;justify-content:center}
.brand-name{font-family:"Josefin Sans",sans-serif;font-weight:700;font-size:15px;color:var(--brown);letter-spacing:.5px}
.premium{position:absolute;left:0;right:0;top:108px;text-align:center;font-family:"Playfair Display",serif;font-style:italic;font-weight:700;font-size:19px;color:var(--cream)}
.premium::before,.premium::after{content:"";display:inline-block;width:44px;height:4px;border-top:1.5px solid var(--cream);border-bottom:1.5px solid var(--cream);vertical-align:middle;margin:0 8px}
.origin{position:absolute;left:0;right:0;top:135px;text-align:center;font-family:"Josefin Sans",sans-serif;font-weight:600;font-size:12.5px;letter-spacing:1.2px;color:var(--cream)}
.product-band{position:absolute;left:4px;right:4px;top:160px;height:29px;background:var(--amber);text-align:center;font-family:"Josefin Sans",sans-serif;font-weight:700;font-size:21px;letter-spacing:1.5px;line-height:33px;color:var(--cream)}
.protein-label{position:absolute;left:5px;top:189px;width:50px;height:136px;display:flex;align-items:center;justify-content:center}
.protein-label span{transform:rotate(-90deg);white-space:nowrap;font-family:"Josefin Sans",sans-serif;font-weight:700;font-size:19px;letter-spacing:1.5px}
.pouch--beef .protein-label{background:var(--beef-strip);color:var(--cream)}
.pouch--mussels .protein-label{background:var(--sea-strip);color:var(--brown)}
.protein-photo{position:absolute;left:55px;right:7px;top:189px;height:136px}
.photo-pasture{background:linear-gradient(180deg,#6f8fa6 0%,#5d7a3c 30%,#7aa23a 60%,#9ab83e 100%)}
.photo-mussels{background:linear-gradient(180deg,#2f6f5f 0%,#4b6a3a 35%,#8a5a28 70%,#5a3a1c 100%)}
.claims-band{position:absolute;left:12px;right:12px;top:325px;height:37px;background:var(--amber);display:flex;justify-content:space-around;align-items:center;padding:0 12px}
.claim{display:flex;flex-direction:column;align-items:center;gap:2px;font-family:"Josefin Sans",sans-serif;font-weight:600;font-size:4.6px;letter-spacing:.3px;color:var(--cream)}
.claim svg{width:17px;height:17px;fill:none;stroke:var(--cream);stroke-width:1.3}
.window{position:absolute;left:82px;width:125px;top:362px;height:40px;background:linear-gradient(180deg,#8d6a4c,#5f4330 60%,#7c5a3e)}
.net{position:absolute;left:0;right:0;top:409px;text-align:center;font-family:"Josefin Sans",sans-serif;font-weight:700;font-size:10px;letter-spacing:.6px;color:var(--cream)}

/* back */
.back-tab{position:absolute;left:95px;width:106px;top:0;height:52px;background:var(--amber);border-radius:0 0 10px 10px;border:1.5px solid var(--cream);border-top:none;display:flex;align-items:center;justify-content:center}
.back-tab .brand-name{color:var(--cream);font-size:15px;letter-spacing:1.2px}
.back-copy{position:absolute;left:22px;right:22px;text-align:center}
.back-heading{top:80px;font-family:"Josefin Sans",sans-serif;font-weight:700;font-size:8.4px;letter-spacing:.6px}
.back-sub{top:93px;font-size:7px;color:var(--ink-soft);letter-spacing:.3px}
.body-text{font-size:5.3px;line-height:1.45;letter-spacing:.2px;text-align:justify;text-align-last:center}
.intro{top:110px}
.why{top:153px;font-family:"Josefin Sans",sans-serif;font-weight:600;font-size:8px;letter-spacing:.5px}
.why-rule{position:absolute;left:109px;width:66px;top:170px;height:1px;background:var(--ink-soft)}
.packed{top:177px;font-size:7px;color:var(--ink-soft);letter-spacing:.3px}
.nutrients{position:absolute;left:0;right:0;top:196px;display:flex;justify-content:center;gap:8px}
.nutrient{width:14px;height:14px;border-radius:50%;background:var(--white);color:var(--sea-blue);font-family:"Josefin Sans",sans-serif;font-weight:700;font-size:6px;display:flex;align-items:center;justify-content:center}
.benefits{top:218px}
.badges{position:absolute;left:0;right:0;top:277px;display:flex;justify-content:center;gap:14px;font-size:5.4px;letter-spacing:.3px}
.badge{display:flex;align-items:center;gap:4px}
.badge svg{width:14px;height:14px;fill:none;stroke:var(--white);stroke-width:1}
.nasties{top:297px;font-size:5.4px}
.pure{top:313px;font-weight:600;font-size:7px;letter-spacing:.3px}
.storage-box{position:absolute;left:27px;right:27px;top:322px;height:31px;border:1px solid var(--ink-soft);display:flex}
.storage-box p{flex:1;padding:3px 5px;font-size:4.6px;line-height:1.35;text-align:justify}
.storage-box p + p{border-left:1px solid var(--ink-soft)}
.label-blank{position:absolute;left:110px;width:62px;top:364px;height:31px;background:var(--white)}
</style>
</head>
<body>
<main class="canvas">

  <section class="pouch pouch--beef" aria-label="Beef liver pouch front">
    <div class="zip-line"></div>
    <div class="brand-tab"></div>
    <div class="brand-seal"><span class="brand-name">BARNEY'S</span></div>
    <p class="premium">Premium</p>
    <p class="origin">AUSTRALIAN GRASS-FED</p>
    <div class="product-band">DOG TREATS</div>
    <div class="protein-label"><span>BEEF LIVER</span></div>
    <div class="protein-photo photo-pasture" role="img" aria-label="Photo of cattle grazing on green pasture beside a barn"></div>
    <div class="claims-band">
      <div class="claim"><svg viewBox="0 0 20 20"><path d="M3 8h10a3 3 0 1 0-3-3M3 12h12a3 3 0 1 1-3 3"/></svg>AIR-DRIED</div>
      <div class="claim"><svg viewBox="0 0 20 20"><path d="M10 17C4 13 4 7 10 3c6 4 6 10 0 14zM10 17V7"/></svg>100% NATURAL</div>
      <div class="claim"><svg viewBox="0 0 20 20"><path d="M4 17L15 4M9 11l-4-1M11 9l-1-4M12 11l4 1M3 3l14 14"/></svg>GRAIN FREE</div>
      <div class="claim"><svg viewBox="0 0 20 20"><circle cx="10" cy="10" r="7.5"/><path d="M8.5 7.5L10.5 6v8"/></svg>SINGLE INGREDIENT</div>
    </div>
    <div class="window" role="img" aria-label="Clear window showing the air-dried treats"></div>
    <p class="net">NET: 70G</p>
  </section>

  <section class="pouch pouch--back" aria-label="Pouch back">
    <div class="zip-line"></div>
    <div class="back-tab"><span class="brand-name">BARNEY'S</span></div>
    <h2 class="back-copy back-heading">FRESH, SMALL-BATCH SUPERFOOD</h2>
    <p class="back-copy back-sub">made with human-grade ingredients</p>
    <p class="back-copy body-text intro">Our premium sardine dog treats are made with the freshest and finest 100% Australian human-grade ingredients. We buy the freshest sardines direct from the Harbourside Fish Market and prepare them in small batches to produce some of the highest quality treats for your precious best friend.</p>
    <h3 class="back-copy why">WHY ARE SARDINES GOOD FOR YOUR DOG?</h3>
    <div class="why-rule"></div>
    <p class="back-copy packed">Packed full of protein and low fat</p>
    <div class="nutrients">
      <span class="nutrient">Ω3</span><span class="nutrient">Ω6</span><span class="nutrient">D</span><span class="nutrient">B12</span><span class="nutrient">Q10</span>
    </div>
    <p class="back-copy body-text benefits">Sardines are rich in omega 3 and 6 fatty acids helping your dog have a wonderfully shiny coat. Vitamin D and B12 helps boost your dog's immune system. Coenzyme Q10 found in sardines are a powerful antioxidant that supports metabolism, cardiovascular health, oxygen utilisation, blood sugar control, and liver detoxification. DHA fatty acids reduce eye disease and help refine memory, learning abilities, and motor skills in puppies. Low calorie, low fat, high protein treat so you don't have to worry about weight gain.</p>
    <div class="badges">
      <span class="badge"><svg viewBox="0 0 20 20"><circle cx="10" cy="10" r="8"/><path d="M8.5 7.5L10.5 6v8"/></svg>SINGLE-INGREDIENT</span>
      <span class="badge"><svg viewBox="0 0 20 20"><path d="M8 3h4M9 3v6L4 17h12l-5-8V3M3 18L17 2"/></svg>PRESERVATIVE-FREE</span>
    </div>
    <p class="back-copy nasties">Don't feed your precious pup any added nasties. Our sardine dog treats are single-ingredient with no added preservatives, salt, or sugar.</p>
    <p class="back-copy pure">Just pure, delicious fish.</p>
    <div class="storage-box">
      <p>Due to the lack of preservatives, it's best to treat your dog within 1 month of opening the resealable bag.</p>
      <p>Please place the bag in a dry area away from the sun. For additional safety, please place opened bags in the fridge.</p>
    </div>
    <div class="label-blank"></div>
    <p class="net">NET: 70G</p>
  </section>

  <section class="pouch pouch--mussels" aria-label="Mussels pouch front">
    <div class="zip-line"></div>
    <div class="brand-tab"></div>
    <div class="brand-seal"><span class="brand-name">BARNEY'S</span></div>
    <p class="premium">Premium</p>
    <p class="origin">AUSTRALIAN CAUGHT</p>
    <div class="product-band">DOG TREATS</div>
    <div class="protein-label"><span>MUSSELS</span></div>
    <div class="protein-photo photo-mussels" role="img" aria-label="Underwater photo of green lip mussels among seaweed"></div>
    <div class="claims-band">
      <div class="claim"><svg viewBox="0 0 20 20"><path d="M3 8h10a3 3 0 1 0-3-3M3 12h12a3 3 0 1 1-3 3"/></svg>AIR-DRIED</div>
      <div class="claim"><svg viewBox="0 0 20 20"><path d="M10 17C4 13 4 7 10 3c6 4 6 10 0 14zM10 17V7"/></svg>100% NATURAL</div>
      <div class="claim"><svg viewBox="0 0 20 20"><path d="M4 17L15 4M9 11l-4-1M11 9l-1-4M12 11l4 1M3 3l14 14"/></svg>GRAIN FREE</div>
      <div class="claim"><svg viewBox="0 0 20 20"><circle cx="10" cy="10" r="7.5"/><path d="M8.5 7.5L10.5 6v8"/></svg>SINGLE INGREDIENT</div>
    </div>
    <div class="window" role="img" aria-label="Clear window showing the air-dried treats"></div>
    <p class="net">NET: 70G</p>
  </section>

</main>
</body>
</html>
```